I want our new logo design to guide the colors and look of the home page. I want it to be vibrant and contemporary. We are a new religious education publishing company. I would like any colors used to describe the product below to be bright and cheerful, but also to look good with our logo colors
On our home page we are introducing a new product for second graders. The product name should look child friendly, but not silly. If there is a way to add reverence to the words FIRST RECONCILIATION and FIRST EUCHARIST, and still make it look like it is a product for children, that would be great.
The product will be called:
Wayfinder Gathering Set for the Welcoming Room
FIRST RECONCILIATION
FIRST EUCHARIST
THE PRODUCT DESCRIPTION SHOULD BE AS FOLLOWS
Field tested and designed for the special needs inclusive classroom
Kit includes high impact visuals, hands-on activities, manipulatives, games, and other teaching aids for total engagement of ALL students
Detailed catechist lesson plans to maximize learning and retention
Cost effective reusable kit
Bilingual
Somewhere it should say COMING SOON, because the product is not ready yet, but we are promoting it. I don't have a picture of this product yet, but above the product description, we need an empty box that we'll use when we're ready to upload the picture of the kit.
There should also be a statement near the product description that says: To learn more about the Wayfinder Set for the Welcoming Room, click here.
Web page links:
About Us
Products
Resources
Contact Us
I would also like a few links to be featured on the home page:
Lanterns Along the Young Road....learn more
"What Calls Us Home?"....learn more
Could It Be Something Else Entirely?...learn more
The Map and the Path...learn more
Open Table Storytelling
I have increased my budget and clarified my brief so that it's easier to understand. It's basically just a home page and a template for the other pages. There is no content on the other web pages that you have to work on. I just need a well designed home page and a nice template for the other pages.
Reason: I am extending the deadline for 2 days so that templates can be designed for 5 additional web pages. Please make each template a little different from the way you designed the home page. These pages can have blank picture boxes and dummy text to save you time. I am only interested in layout for the addtional pages. Thank you!
We've made a selection and wanted to thank all of you for your wonderful designs!

```html
<!DOCTYPE html>
<html lang="en">
<head>
<meta charset="utf-8">
<title>Harbor Light Catechetics</title>
<link href="https://fonts.googleapis.com/css2?family=Noto+Sans:wght@400;700&family=Amatic+SC:wght@700&display=swap" rel="stylesheet">
<style>
  :root {
    --page-bg: #ece5d9;
    --card-bg: #f4f2ee;
    --orange: #f39a12;
    --orange-soft: #f6dfbd;
    --brand-red: #c0202e;
    --brown: #7a4b2b;
    --rule: #d9d4cc;
  }
  * { margin: 0; padding: 0; box-sizing: border-box; }
  html, body { width: 1200px; height: 1000px; overflow: hidden; }
  body {
    background: var(--page-bg);
    font-family: "Noto Sans", Verdana, sans-serif;
    color: var(--brown);
  }
  .stage {
    width: 960px; height: 800px; position: relative;
    transform: scale(1.25); transform-origin: 0 0;
  }
  .sheet {
    position: absolute; left: 40px; top: 40px; width: 880px; height: 670px;
    background: var(--card-bg);
    box-shadow: 0 2px 6px rgba(90, 70, 40, .25);
  }
  .sheet-band {
    position: absolute; left: 0; bottom: 0; width: 100%; height: 13px;
    background: var(--orange);
  }
  .brand {
    position: absolute; left: 20px; top: 34px;
    display: flex; align-items: center; gap: 10px;
  }
  .brand-dot { width: 22px; height: 22px; border-radius: 50%; background: var(--orange); }
  .brand-name { font-size: 21px; font-weight: 400; color: var(--brand-red); letter-spacing: -.2px; }
  .main-nav {
    position: absolute; left: 450px; top: 41px;
    font-size: 14.5px; font-weight: 700; color: var(--orange);
  }
  .main-nav a { color: var(--orange); text-decoration: none; }
  .product-title {
    position: absolute; left: 19px; top: 136px; width: 400px;
    font-size: 14.5px; line-height: 18px; font-weight: 700; color: var(--orange);
  }
  .sacrament-names {
    position: absolute; left: 19px; top: 207px;
    font-family: "Amatic SC", cursive; font-weight: 700;
    font-size: 40px; line-height: 48px; color: var(--orange);
  }
  .art {
    position: absolute; background: var(--orange-soft); opacity: .75; border-radius: 8px;
  }
  .art-chalice { left: 278px; top: 200px; width: 62px; height: 90px; border-radius: 30px 30px 10px 10px; }
  .art-candle { left: 358px; top: 170px; width: 46px; height: 88px; }
  .art-figures { left: 55px; top: 472px; width: 72px; height: 64px; border-radius: 30px; }
  .features {
    position: absolute; left: 19px; top: 312px; width: 420px;
    list-style: none; font-size: 12.3px; line-height: 19.2px;
  }
  .features li { padding-left: 10px; text-indent: -10px; }
  .features li::before { content: "- "; }
  .coming-soon {
    position: absolute; left: 155px; top: 476px;
    font-family: "Amatic SC", cursive; font-weight: 700; font-size: 30px; color: var(--orange);
  }
  .learn-statement {
    position: absolute; left: 19px; top: 532px; width: 415px;
    font-size: 11.5px; line-height: 16px; color: var(--brown);
  }
  .learn-statement a { color: var(--orange); text-decoration: none; font-weight: 700; }
  .column-divider {
    position: absolute; left: 441px; top: 140px; width: 1px; height: 420px; background: var(--rule);
  }
  .image-box {
    position: absolute; left: 450px; top: 140px; width: 410px; height: 300px;
    border: 3px solid var(--orange);
    display: flex; align-items: center; justify-content: center;
    font-size: 13.5px; line-height: 21px; color: var(--orange);
  }
  .thumbs { position: absolute; left: 450px; top: 460px; display: flex; gap: 1px; }
  .thumb { width: 136px; height: 100px; border: 1px solid var(--orange); }
  .footer-rule { position: absolute; left: 20px; top: 579px; width: 840px; height: 1px; background: var(--rule); }
  .feature-links { position: absolute; top: 592px; list-style: none; font-size: 11px; line-height: 18.6px; }
  .feature-links.col-a { left: 19px; }
  .feature-links.col-b { left: 333px; }
  .feature-links a { color: var(--orange); text-decoration: none; }
</style>
</head>
<body>
<div class="stage">
  <div class="sheet">
    <header>
      <div class="brand">
        <span class="brand-dot"></span>
        <span class="brand-name">Harbor Light Catechetics</span>
      </div>
      <nav class="main-nav">
        <a href="#">About Us</a> | <a href="#">Products</a> | <a href="#">Resources</a> | <a href="#">Contact Us</a>
      </nav>
    </header>

    <h1 class="product-title">Wayfinder Gathering Set for the Welcoming Room</h1>
    <h2 class="sacrament-names">First Reconciliation<br>First Eucharist</h2>
    <div class="art art-chalice" role="img" aria-label="Sketched chalice drawing"></div>
    <div class="art art-candle" role="img" aria-label="Sketched lit candle drawing"></div>

    <ul class="features">
      <li>field tested and designed for the special needs inclusive<br>classroom</li>
      <li>kit includes high impact visuals, hands-on activities, manipulatives,<br>games, and other teaching aids for total engagement of<br>ALL students</li>
      <li>detailed catechist lesson plans to maximize learning and retention</li>
      <li>cost effective reusable kit.</li>
      <li>bilingual</li>
    </ul>

    <div class="art art-figures" role="img" aria-label="Sketched figures drawing"></div>
    <p class="coming-soon">Coming Soon</p>
    <p class="learn-statement">To learn more about the Wayfinder Set for the Welcoming Room, <a href="#">click here</a>.</p>

    <div class="column-divider"></div>
    <div class="image-box"><span>image box<br>410x300px</span></div>
    <div class="thumbs">
      <div class="thumb"></div><div class="thumb"></div><div class="thumb"></div>
    </div>

    <div class="footer-rule"></div>
    <ul class="feature-links col-a">
      <li>Lanterns Along the Young Road <a href="#">...learn more</a></li>
      <li>"What Calls Us Home?" <a href="#">...learn more</a></li>
      <li>Could It Be Something Else Entirely? <a href="#">...learn more</a></li>
    </ul>
    <ul class="feature-links col-b">
      <li>The Map and the Path <a href="#">...learn more</a></li>
      <li>Open Table Storytelling <a href="#">...learn more</a></li>
    </ul>

    <div class="sheet-band"></div>
  </div>
</div>
</body>
</html>
```